Mobile (Android/iPhone) game studio needs stationary design and a business card

We are Plunk Ferret Software and we need a fun and creative stationary design. Our company builds Android and iPhone games and children's software. The stationary designs should reflect an entertainment, fun and creativity. The pieces of stationary we need are:
1. A4 and Letter Word template (company letterhead)
2. A4 and Letter PPT template
3. Business card
4. Envelopes of various standard sizes
Each of the designs should somehow utilize our company logo.
The business card should have the following:
1. Incorporates our company logo (see attached)
2. Has a front and back with the same design (front is English, back is Traditional Chinese)
3. Delivered in an editable template so we can easily add new business cards using the same template when we hire more employees
4. Field for full name
5. Field for employee's title
6. Field for employee's email address
7. Field for company phone number - +886-2-51384470
8. Field for mobile phone number
9. Field for company fax number - +886-2-51384492
10. Company website address: www.plunkferret.example
11. Company address (on English side): 7F-2, NO. 63, Lane 91, Guoyuan Road, Dali District, Taipei Taiwan
12. Company address (on Traditional Chinese side): See Word document attachment for address in Chinese characters
Industry/Entity Type
Games
Look and feel
Each slider illustrates characteristics of the customer's brand and the style your logo design should communicate.

```html
<!DOCTYPE html>
<html lang="en">
<head>
<meta charset="utf-8">
<title>Plunk Ferret Software – Business Card</title>
<link rel="stylesheet" href="https://fonts.googleapis.com/css2?family=Questrial&family=Noto+Sans+TC:wght@400;500&display=swap">
<style>
  :root {
    --page-bg: #e9e7e3;
    --card-white: #ffffff;
    --blue-light: #55b8ec;
    --blue-mid: #2a8ad6;
    --blue-deep: #1665b8;
    --brand-blue: #1f7fc8;
    --text-grey: #5a5d62;
    --text-dark: #3c3f44;
    --white: #ffffff;
  }
  * { margin: 0; padding: 0; box-sizing: border-box; }
  html, body {
    width: 1200px;
    height: 900px;
    overflow: hidden;
  }
  body {
    background: var(--page-bg);
    font-family: "Questrial", sans-serif;
    position: relative;
  }
  .card {
    position: absolute;
    left: 250px;
    width: 700px;
    height: 400px;
    border-radius: 28px;
    overflow: hidden;
    box-shadow: 0 6px 18px rgba(0, 0, 0, 0.15);
  }

  /* Chinese side */
  .card--front {
    top: 35px;
    background: linear-gradient(180deg, var(--blue-light) 0%, var(--blue-mid) 55%, var(--blue-deep) 100%);
    color: var(--white);
    text-align: center;
  }
  .front-brand {
    position: absolute;
    top: 110px;
    left: 0;
    right: 0;
    display: flex;
    align-items: center;
    justify-content: center;
    gap: 16px;
  }
  .brand-dot {
    width: 62px;
    height: 62px;
    border-radius: 50%;
    flex: none;
  }
  .front-brand .brand-dot { background: var(--white); }
  .front-brand .brand-name {
    font-size: 30px;
    color: var(--white);
  }
  .front-address {
    position: absolute;
    top: 272px;
    left: 0;
    right: 0;
    font-family: "Noto Sans TC", sans-serif;
    font-size: 21px;
    letter-spacing: 2px;
  }
  .front-web {
    position: absolute;
    top: 312px;
    left: 0;
    right: 0;
    font-size: 16px;
    letter-spacing: 2.5px;
  }

  /* English side */
  .card--back {
    top: 465px;
    background: var(--card-white);
    color: var(--text-grey);
  }
  .back-brand {
    position: absolute;
    top: 80px;
    left: 40px;
    display: flex;
    align-items: center;
    gap: 14px;
  }
  .back-brand .brand-dot { background: var(--brand-blue); width: 56px; height: 56px; }
  .back-brand .brand-name {
    font-size: 26px;
    color: var(--brand-blue);
  }
  .person {
    position: absolute;
    top: 38px;
    right: 40px;
    text-align: right;
  }
  .person-name {
    font-size: 22px;
    color: var(--brand-blue);
    font-weight: 700;
  }
  .person-title {
    font-size: 16px;
    color: var(--text-dark);
    margin-top: 4px;
  }
  .person-mobile {
    font-size: 15px;
    margin-top: 3px;
    display: flex;
    align-items: center;
    justify-content: flex-end;
    gap: 5px;
  }
  .company-details {
    position: absolute;
    left: 70px;
    top: 238px;
  }
  .company-address {
    font-size: 19px;
    line-height: 25px;
    color: var(--text-dark);
    font-weight: 700;
  }
  .contact-row {
    display: flex;
    align-items: center;
    gap: 6px;
    font-size: 18px;
    margin-top: 8px;
  }
  .contact-row .gap { width: 10px; }
  .icon { width: 16px; height: 16px; fill: var(--brand-blue); flex: none; }
  .mascot-area {
    position: absolute;
    right: 28px;
    bottom: 22px;
    width: 210px;
    height: 200px;
    border-radius: 50%;
    background: radial-gradient(circle at 40% 35%, #6cc3f0 0%, #2a8ad6 60%, #1a66b3 100%);
  }
</style>
</head>
<body>

  <section class="card card--front" aria-label="Business card, Chinese side">
    <div class="front-brand">
      <span class="brand-dot"></span>
      <span class="brand-name">Plunk Ferret Software</span>
    </div>
    <p class="front-address" lang="zh-Hant">台灣台北市大理區國園路91巷63號7樓之2</p>
    <p class="front-web">www.plunkferret.example</p>
  </section>

  <section class="card card--back" aria-label="Business card, English side">
    <div class="back-brand">
      <span class="brand-dot"></span>
      <span class="brand-name">Plunk Ferret Software</span>
    </div>

    <div class="person">
      <p class="person-name">Dana Whitlock</p>
      <p class="person-title">Senior Researcher</p>
      <p class="person-mobile">
        <svg class="icon" viewBox="0 0 16 16" aria-hidden="true"><rect x="4" y="1" width="8" height="14" rx="1.5"/><rect x="5.5" y="3" width="5" height="8" fill="#fff"/></svg>
        +886-2-60917735
      </p>
    </div>

    <div class="company-details">
      <p class="company-address">7F-2, NO. 63, Lane 91, Guoyuan Road,<br>Dali District, Taipei Taiwan</p>
      <p class="contact-row">
        <svg class="icon" viewBox="0 0 16 16" aria-hidden="true"><path d="M1 5c0-2 3-3 7-3s7 1 7 3v1h-4V5H5v1H1z"/><path d="M3 7h10l1 7H2z"/></svg>
        <span>+886-2-51384470</span>
        <span class="gap"></span>
        <svg class="icon" viewBox="0 0 16 16" aria-hidden="true"><rect x="4" y="1" width="8" height="5"/><rect x="1" y="6" width="14" height="6" rx="1"/><rect x="4" y="10" width="8" height="5" fill="#fff" stroke="#1f7fc8"/></svg>
        <span>+886-2-51384492</span>
      </p>
      <p class="contact-row">
        <svg class="icon" viewBox="0 0 16 16" aria-hidden="true"><rect x="1" y="3" width="14" height="10" rx="1"/><path d="M2 4l6 5 6-5" fill="none" stroke="#fff" stroke-width="1.3"/></svg>
        <span>info@plunkferret.example</span>
      </p>
    </div>

    <div class="mascot-area" role="img" aria-label="Company mascot illustration"></div>
  </section>

</body>
</html>
```